Every Drawer Neatly Sorted or EDN Organized needs a business card design. EDN Organized is a professi

We need a business card design that is clean, sharp and conveys a sense of organization. I already have a logo.

Target Market(s)

Families (specifically mothers), small business owners, parents, seniors

Industry/Entity Type

Business

Contact Information for Business Card

My website is www.ednorganized-example.com and my Facebook page is http://www.socialpage-example.com/everydrawerneatlysorted. The phone number is 555-418-2706 and I want to be listed as Miriel O. Dunsford, Owner

Requirements
Must have
• My logo.

```html
<!DOCTYPE html>
<html lang="en">
<head>
<meta charset="utf-8">
<title>EDN Organized – Business Card</title>
<link rel="stylesheet" href="https://fonts.googleapis.com/css2?family=Exo+2:ital,wght@1,800&family=Raleway:wght@300;400&display=swap">
<style>
  :root {
    --paper: #e9eaea;
    --ink: #141718;
    --sky: #3db9f5;
    --white: #ffffff;
    --logo-ink: #1b1b1b;
  }
  html, body {
    margin: 0;
    padding: 0;
    overflow: hidden;
    background: var(--paper);
  }
  .card {
    position: relative;
    width: 1200px;
    height: 720px;
    background: var(--paper);
    overflow: hidden;
  }
  .card-bands {
    position: absolute;
    inset: 0;
  }
  .brand-name {
    position: absolute;
    top: 138px;
    left: 0;
    width: 1200px;
    text-align: center;
    margin: 0;
    font-family: "Raleway", sans-serif;
    font-weight: 400;
    font-size: 46px;
    line-height: 1.2;
    letter-spacing: 3px;
    color: var(--logo-ink);
  }
  .owner-line {
    position: absolute;
    top: 214px;
    left: 0;
    width: 1200px;
    text-align: center;
    margin: 0;
    font-family: "Raleway", sans-serif;
    font-weight: 400;
    font-size: 20px;
    letter-spacing: 3px;
    color: var(--logo-ink);
  }
  .contact-text {
    position: absolute;
    margin: 0;
    font-family: "Exo 2", sans-serif;
    font-style: italic;
    font-weight: 800;
    line-height: 1;
    color: var(--white);
    white-space: nowrap;
  }
  .phone-number {
    left: 114px;
    top: 484px;
    font-size: 34px;
  }
  .social-address {
    right: 180px;
    top: 490px;
    font-size: 13.5px;
    letter-spacing: 0.4px;
  }
  .web-address {
    right: 213px;
    top: 619px;
    font-size: 27px;
    letter-spacing: 1px;
  }
  .brand-monogram {
    position: absolute;
    left: 80px;
    top: 570px;
    margin: 0;
    font-family: "Raleway", sans-serif;
    font-weight: 300;
    font-size: 108px;
    line-height: 1;
    color: var(--white);
    letter-spacing: 4px;
  }
  .icon {
    position: absolute;
  }
</style>
</head>
<body>
<main class="card">
  <svg class="card-bands" width="1200" height="720" viewBox="0 0 1200 720" aria-hidden="true">
    <polygon fill="var(--sky)" points="0,379 443,379 605,286 768,379 1200,379 1200,720 0,720"/>
    <polygon fill="var(--ink)" points="0,397 460,397 605,313 750,397 1200,397 1200,711 0,711"/>
  </svg>

  <h1 class="brand-name">Every Drawer Neatly Sorted</h1>
  <p class="owner-line">Miriel O. Dunsford, Owner</p>

  <p class="contact-text phone-number">555-418-2706</p>

  <svg class="icon phone-icon" style="left:423px;top:456px" width="82" height="82" viewBox="0 0 82 82" aria-hidden="true">
    <circle cx="41" cy="41" r="41" fill="var(--sky)"/>
    <rect x="29" y="17" width="24" height="48" rx="4" fill="none" stroke="var(--white)" stroke-width="2.5"/>
    <line x1="29" y1="25" x2="53" y2="25" stroke="var(--white)" stroke-width="2"/>
    <line x1="29" y1="55" x2="53" y2="55" stroke="var(--white)" stroke-width="2"/>
    <circle cx="41" cy="60" r="2.2" fill="var(--white)"/>
  </svg>

  <p class="contact-text social-address">WWW.SOCIALPAGE-EXAMPLE.COM/EVERYDRAWERNEATLYSORTED</p>

  <svg class="icon social-icon" style="left:1053px;top:456px" width="82" height="82" viewBox="0 0 82 82" aria-hidden="true">
    <circle cx="41" cy="41" r="41" fill="var(--sky)"/>
  </svg>

  <p class="brand-monogram">EDN</p>

  <p class="contact-text web-address">WWW.EDNORGANIZED-EXAMPLE.COM</p>

  <svg class="icon globe-icon" style="left:1053px;top:591px" width="82" height="82" viewBox="0 0 82 82" aria-hidden="true">
    <circle cx="41" cy="41" r="41" fill="var(--sky)"/>
    <g fill="none" stroke="var(--white)" stroke-width="3">
      <circle cx="41" cy="41" r="20"/>
      <ellipse cx="41" cy="41" rx="9" ry="20"/>
      <line x1="41" y1="21" x2="41" y2="61"/>
      <line x1="21" y1="41" x2="61" y2="41"/>
      <line x1="24" y1="31" x2="58" y2="31"/>
      <line x1="24" y1="51" x2="58" y2="51"/>
    </g>
  </svg>
</main>
</body>
</html>
```